Anatomic 3D models + Urological Robotic surgery site

I want a website to represent my business as a developer of 3D models (reconstructions based on CT and MRI scans) and urological robotic surgery. The main point I need on my website is that it is modern, very attractive, clean, responsive and an interaction that differentiate me from the usual websites they have in my market. The site will be in portuguese and I'll provide the content to be used. The company name would be my name: Dr Mateus Vilhena. The colors and other choices I made here are not final decisions. If you have a suggestion you, they are welcome.

Target Market(s)

My patients

Industry/Entity Type

Medical

Coding

Number of Pages Required

1 page

Font styles to use
Sans Serif

Colors
0054AA
0677BA
7BADD7
CADEEF
E8F1F8
0094D4
00A9DD
6FCCEA
C7EBF8
E9F6FB
00AB8E
00BBA5
67D7C9
C6EFE9
E9F9F6
59FF00
82FF00
B8FF75
E3FFCB
F4FFEA
FFC000
F8CF3A
FAE287
FDF2CF
FEFAEE
F0912C
F2A743
F7CA91
FBE8D2
FDF5EE
A7469A
B969AE
D3A5CF
EDDBEB
F8F0F9
6B429C
8869AF
B7A5CE
E3DAEB
F3F0F8

Requirements
Must have
• Responsive, clean, modern, attractive, stand out from usual sites.
Should not have
• Antiquate boring designs.

```html
<!DOCTYPE html>
<html lang="pt-BR">
<head>
<meta charset="utf-8">
<title>Dr. Mateus Vilhena — Urologia e Cirurgia Robótica</title>
<link href="https://fonts.googleapis.com/css2?family=Plus+Jakarta+Sans:wght@400;500;600;700&display=swap" rel="stylesheet">
<style>
:root{
  --blue:#0054AA;
  --blue-mid:#0677BA;
  --blue-soft:#CADEEF;
  --blue-pale:#E8F1F8;
  --navy:#0B3C7C;
  --teal:#00AB8E;
  --ink:#111418;
  --white:#fff;
}
*{box-sizing:border-box;margin:0;padding:0}
html,body{width:1200px;height:4428px;overflow:hidden}
body{font-family:"Plus Jakarta Sans",sans-serif;color:var(--ink);background:var(--white);position:relative}
.abs{position:absolute}
a{color:inherit;text-decoration:none}
ul{padding-left:24px}

/* hero */
.hero{left:0;top:0;width:1200px;height:332px;background:linear-gradient(110deg,#fff 30%,var(--blue-pale) 65%,#d6e6f4 100%)}
.brand{left:76px;top:36px;font-size:29px;font-weight:600;color:var(--blue)}
.nav{left:522px;top:40px;display:flex;gap:20px;font-size:19px;font-weight:600}
.btn{display:inline-flex;align-items:center;justify-content:center;border-radius:6px;font-weight:600}
.btn-primary{background:var(--blue);color:#fff}
.btn-ghost{border:1.5px solid var(--teal);color:var(--blue);background:#fff}
.nav-cta{left:963px;top:30px;width:160px;height:45px;font-size:19px}
.hero-title{left:76px;top:172px;font-size:39px;font-weight:600;line-height:1.25}
.hero-title em{font-style:normal;color:var(--blue)}
.hero-lead{left:607px;top:132px;width:510px;font-size:18px;line-height:1.3}
.hero-actions{left:607px;top:244px;display:flex;gap:16px}
.hero-actions .btn{height:45px;font-size:13px}
.photo{background:linear-gradient(120deg,#3b6fc0,#7ea6de 45%,#c9d6e4 70%,#5b84c6)}
.hero-photo{left:0;top:332px;width:1200px;height:373px}

/* about */
.about{left:76px;top:786px;width:1047px;height:463px;border-radius:36px;background:linear-gradient(90deg,#dfe9f4,#e9f0f8)}
.eyebrow{font-size:19px;color:var(--blue)}
.about .eyebrow{left:64px;top:74px}
.about h2{left:64px;top:110px;font-size:25px;font-weight:600}
.about .bio{left:64px;top:172px;width:280px;font-size:18px;letter-spacing:-.2px;line-height:1.33;color:var(--blue)}
.about-portrait{left:370px;top:50px;width:300px;height:413px;background:linear-gradient(180deg,#cfdbe8,#f1f4f8)}
.about blockquote{left:580px;top:230px;width:403px;height:176px;background:#fff;border-radius:12px;padding:26px 24px 0 38px;font-size:18px;line-height:1.33;color:var(--blue)}
.about blockquote::before{content:"";position:absolute;left:26px;top:26px;width:2px;height:124px;background:var(--blue-soft)}

/* section titles */
.sec-title{left:0;width:1200px;text-align:center;font-size:25px;font-weight:600}
.sec-sub{left:0;width:1200px;text-align:center;font-size:19px;line-height:1.27}

/* approach cards */
.card{background:#fff;border-radius:12px;box-shadow:0 2px 5px rgba(0,0,0,.18);overflow:hidden}
.approach{top:1430px;width:340px;height:452px}
.approach .photo{height:232px}
.approach h3{margin:32px 22px 16px;font-size:18px;letter-spacing:-.3px;font-weight:600;white-space:nowrap}
.approach p{margin:0 22px;font-size:18px;letter-spacing:-.2px;line-height:1.33}

/* 3D planning */
.plan{left:76px;top:1952px;width:1047px;height:578px;border-radius:36px;background:var(--blue-pale)}
.plan .eyebrow{left:54px;top:78px}
.plan h2{left:54px;top:124px;font-size:27px;font-weight:600;line-height:1.3}
.plan .body{left:54px;top:214px;width:425px;font-size:18px;line-height:1.33;color:var(--blue)}
.plan .benefits{left:54px;top:386px;width:430px;font-size:18px;line-height:1.33;color:var(--blue)}
.frame{left:498px;top:80px;width:500px;height:418px;border:3px solid var(--teal)}
.model{left:512px;top:92px;width:474px;height:392px;background:linear-gradient(135deg,#4a90d8,#7a64a8 35%,#d4574a 55%,#c9b07a 80%,#5a9bd8)}
.dot{width:40px;height:40px;border-radius:50%;background:var(--blue)}

/* services */
.service{top:2747px;width:518px;height:368px}
.service .ico{position:absolute;left:52px;top:44px}
.service h3{position:absolute;left:130px;top:48px;font-size:18px;font-weight:600;line-height:1.33}
.service ul{position:absolute;left:36px;font-size:18px;line-height:1.33}

/* commitment */
.commit{left:0;top:3206px;width:1200px;height:253px;background:var(--blue);color:#fff;text-align:center}
.commit h2{margin-top:54px;font-size:25px;font-weight:600}
.commit p{margin:28px auto 0;width:950px;font-size:18px;line-height:1.33;color:#dbe8f6}

/* contact */
.contact-bg{left:0;top:3767px;width:1200px;height:661px;background:var(--navy)}
.contact{left:165px;top:3555px;width:869px;height:516px;border-radius:14px;background:var(--blue-pale);overflow:hidden}
.contact h2{left:53px;top:58px;font-size:25px;font-weight:600}
.contact .lead{left:53px;top:112px;width:400px;font-size:18px;line-height:1.33;color:var(--blue)}
.contact dl{left:53px;top:200px;font-size:18px;line-height:1.33}
.contact dt{color:var(--blue)}
.contact dd{margin-bottom:22px}
.contact .btn{left:53px;top:420px;width:188px;height:44px;font-size:12px}
.contact-panel{left:510px;top:80px;width:280px;height:436px;background:#c4d9ee}
.contact-portrait{left:490px;top:140px;width:300px;height:376px;background:linear-gradient(180deg,#d7e0ea,#f4f6f9);border:3px solid var(--teal);border-bottom:0}
.chat{left:-20px;top:3982px;width:120px;height:66px;border-radius:0 33px 33px 0;background:var(--blue)}
.chat span{position:absolute;left:52px;top:13px;width:40px;height:40px;border-radius:50%;background:#fff}

/* footer */
.foot-brand{left:76px;top:4122px;font-size:25px;font-weight:600;color:#fff}
.foot-tag{left:76px;top:4168px;width:200px;font-size:18px;line-height:1.33;color:#dce7f5}
.foot-col{top:4124px;font-size:13px;color:#fff}
.foot-col h4{font-size:14px;font-weight:600;margin-bottom:24px}
.foot-col li{list-style:none;margin-bottom:26px}
.news{left:855px;top:4120px;width:268px;height:170px;border-radius:8px;background:#2b5a9a;color:#fff;padding:18px 12px}
.news h4{font-size:15px;font-weight:600;line-height:1.3}
.news form{display:flex;margin-top:18px;height:34px}
.news input{flex:1;border:0;font:10px "Plus Jakarta Sans",sans-serif;padding:0 8px;width:150px}
.news button{border:0;background:#7b3fa0;color:#fff;font:600 11px "Plus Jakarta Sans",sans-serif;padding:0 10px}
.news small{display:block;margin-top:10px;font-size:10px;line-height:1.3;color:#c9d6ea}
.foot-rule{left:76px;top:4350px;width:1047px;height:1px;background:#3a64a0}
.legal{left:0;top:4378px;width:1200px;text-align:center;font-size:11px;color:#fff;line-height:2}
.legal small{display:block;font-size:10px;color:#b8c8e0}
</style>
</head>
<body>

<header class="abs hero"></header>
<a class="abs brand" href="#">Dr. Mateus Vilhena</a>
<nav class="abs nav"><a href="#sobre">Sobre</a><a href="#abordagem">Abordagem</a><a href="#tecnologia">Tecnologia 3D</a><a href="#servico">Serviço</a></nav>
<a class="abs btn btn-primary nav-cta" href="#contato">Consulta</a>
<h1 class="abs hero-title">Cuidando com precisão,<br>tratando <em>com empatia</em></h1>
<p class="abs hero-lead">Usamos tecnologias avançadas, como cirurgia robótica, somente quando absolutamente apropriado, com uma abordagem que prioriza as necessidades individuais e a empatia.</p>
<div class="abs hero-actions">
  <a class="btn btn-primary" style="width:162px" href="#contato">consulte agora</a>
  <a class="btn btn-ghost" style="width:230px" href="#abordagem">conheça nossa abordagem</a>
</div>
<div class="abs photo hero-photo" role="img" aria-label="Equipe cirúrgica com toucas e máscaras durante uma cirurgia"></div>

<section class="abs about" id="sobre">
  <p class="abs eyebrow">About Us</p>
  <h2 class="abs">Dr. Mateus Vilhena</h2>
  <p class="abs bio">Sou urologista com foco em cirurgia robótica e atendimento integral ao paciente. Mais do que técnica, acredito que uma boa medicina começa com escuta, planejamento cuidadoso e comprometimento em oferecer o melhor para cada paciente.</p>
  <div class="abs about-portrait" role="img" aria-label="Retrato de médica de jaleco branco, máscara e estetoscópio"></div>
  <blockquote class="abs">“Minha missão é oferecer cuidados baseados em ciência, tecnologia e humanidade — respeitando o tempo, as escolhas e os objetivos de cada paciente.”</blockquote>
</section>

<h2 class="abs sec-title" id="abordagem" style="top:1302px">Nossa abordagem</h2>
<p class="abs sec-sub" style="top:1345px">Nem todo tratamento requer cirurgia. Nem toda<br>operação precisa ser feita com um robô.</p>

<article class="abs card approach" style="left:76px">
  <div class="photo" style="background:linear-gradient(120deg,#e8ecef,#c9cfd6 50%,#f2efe9)" role="img" aria-label="Médico conversando com paciente em consultório"></div>
  <h3>Diretrizes Médicas Atuais</h3>
  <p>Seguimos as mais recentes diretrizes médicas internacionais para garantir que o tratamento atenda aos padrões globais.</p>
</article>
<article class="abs card approach" style="left:430px">
  <div class="photo" style="background:linear-gradient(120deg,#f5f6f8,#dde2e8 55%,#2a3140)" role="img" aria-label="Aperto de mão entre mão robótica e mão humana"></div>
  <h3>Suporte de Inteligência Artificial</h3>
  <p>Usando tecnologia de IA para dar suporte à tomada de decisões clínicas mais precisas e personalizadas.</p>
</article>
<article class="abs card approach" style="left:784px">
  <div class="photo" style="background:linear-gradient(120deg,#6b6f74,#a89a88 50%,#3f4a5a)" role="img" aria-label="Grupo de pessoas conversando em torno de uma mesa"></div>
  <h3>Comunicação aberta</h3>
  <p>Temos conversas abertas sobre as reais necessidades, benefícios e riscos de cada abordagem.</p>
</article>

<section class="abs plan" id="tecnologia">
  <p class="abs eyebrow">Planejamento com Tecnologia 3D</p>
  <h2 class="abs">Olhando além da imagem:<br>planejando em profundidade.</h2>
  <p class="abs body">Na cirurgia renal e de próstata, adotamos o uso de modelos 3D personalizados, criados a partir dos resultados dos exames do próprio paciente. Este modelo ajuda a entender a anatomia com precisão, facilitando a seleção da melhor abordagem cirúrgica.</p>
  <div class="abs benefits">Benefícios comprovados:
    <ul><li>Reduz o sangramento durante a cirurgia</li><li>Tempo de operação mais curto</li><li>Mudanças de estratégia em quase metade dos casos avaliados</li></ul>
  </div>
  <div class="abs frame"></div>
  <div class="abs model" role="img" aria-label="Modelo anatômico 3D de rins, vasos sanguíneos e pelve"></div>
  <span class="abs dot" style="left:928px;top:48px"></span>
  <span class="abs dot" style="left:514px;top:490px"></span>
</section>

<h2 class="abs sec-title" id="servico" style="top:2592px">Serviços abrangentes</h2>
<p class="abs sec-sub" style="top:2635px">Acompanhamos você antes, durante e depois do procedimento<br>para garantir uma experiência completa de tratamento.</p>

<article class="abs card service" style="left:76px">
  <svg class="ico" width="60" height="66" viewBox="0 0 60 66" aria-hidden="true"><rect x="3" y="8" width="54" height="55" rx="4" fill="none" stroke="#0054AA" stroke-width="5"/><rect x="18" y="2" width="24" height="12" rx="3" fill="#0054AA"/><path d="M15 37l10 10 20-20" fill="none" stroke="#0054AA" stroke-width="5"/></svg>
  <h3>Suporte Pré-Procedimento<br>Seu foco deve ser na saúde, não<br>na burocracia.</h3>
  <ul style="top:192px;width:450px"><li>Uma equipe dedicada que cuida de todos os assuntos administrativos com hospitais e seguros de saúde.</li><li>Suporte próximo, rápido e humano, para que você possa se concentrar na sua preparação e bem-estar.</li></ul>
</article>
<article class="abs card service" style="left:607px">
  <svg class="ico" width="70" height="56" viewBox="0 0 70 56" aria-hidden="true"><path d="M18 44a14 14 0 0 1-2-28 18 18 0 0 1 34 2 12 12 0 0 1 4 24" fill="none" stroke="#0054AA" stroke-width="4"/><path d="M26 30l-6 7 6 7M44 38l6-7-6-7" fill="none" stroke="#0054AA" stroke-width="4"/></svg>
  <h3 style="left:158px">Cuidados Pós-Operatórios<br>Uma boa recuperação é uma<br>parte importante do tratamento.</h3>
  <ul style="top:172px;width:460px"><li>Visitas domiciliares por enfermeiros e fisioterapeutas, se necessário</li><li>Um guia prático sobre atividade, nutrição e medicação</li><li>Monitoramento de sinais que requerem atenção com supervisão clínica cuidadosa</li><li>Canal de contato direto para dúvidas e suporte</li></ul>
</article>

<section class="abs commit">
  <h2>Nosso Compromisso</h2>
  <p>Acreditamos que os melhores resultados vêm de uma combinação de conhecimento, tecnologia e empatia. Nosso compromisso é entender profundamente o que você está enfrentando, apresentar com clareza todas as opções disponíveis e construir, juntos, o melhor caminho para o seu tratamento. Porque cada paciente é único — e merece ser tratado como tal.</p>
</section>

<div class="abs contact-bg"></div>
<section class="abs contact" id="contato">
  <h2 class="abs">Comece sua jornada de tratamento</h2>
  <p class="abs lead">Pronto para discutir as melhores opções de tratamento para você? Entre em contato conosco para consulta ou mais informações.</p>
  <dl class="abs">
    <dt>Telepon</dt><dd>+55 (XX) XXXX-XXXX</dd>
    <dt>Email</dt><dd>contato@drmateusvilhena.com</dd>
    <dt>Alamat</dt><dd>Rua das Acácias, 250 - São Paulo</dd>
  </dl>
  <a class="abs btn btn-primary" href="#">Marque uma consulta agora</a>
  <div class="abs contact-panel"></div>
  <div class="abs contact-portrait" role="img" aria-label="Retrato de médica de jaleco branco, máscara e estetoscópio"></div>
</section>
<div class="abs chat"><span></span></div>

<footer>
  <p class="abs foot-brand">Dr. Mateus Vilhena</p>
  <p class="abs foot-tag">Cuidando com precisão, tratando com empatia</p>
  <div class="abs foot-col" style="left:341px"><h4>Empresa</h4><ul style="padding:0"><li><b>Sobre</b></li><li>Abordagem</li></ul></div>
  <div class="abs foot-col" style="left:498px"><h4>Jurídico</h4><ul style="padding:0"><li>política de Privacidade</li><li>Termos e Serviços</li><li>Termos de Uso</li><li>Política de Reembolso</li></ul></div>
  <div class="abs foot-col" style="left:692px"><h4>Links rápidos</h4><ul style="padding:0"><li>Tecnologia 3D</li><li>Serviço</li></ul></div>
  <div class="abs news">
    <h4>Join Our NeAssine nossa newsletter</h4>
    <form><input type="email" placeholder="Seu endereço de email"><button type="button">Inscrever-se</button></form>
    <small>* Enviaremos atualizações semanais para melhor gerenciamento de ferramentas.</small>
  </div>
  <div class="abs foot-rule"></div>
  <p class="abs legal">Dr. Mateus Vilhena- All Rights Reserved. Copyright © 2025<small>As informações neste site não pretendem substituir aconselhamento médico profissional, diagnóstico ou tratamento.</small></p>
</footer>
</body>
</html>
```